TRAVo Kiosk Webpage Design

Just need a simple, single page web design. I have a preliminary idea of what I need, just want to add a professional touch to it. We already have the google map locator plug-in. Generic website is already up and I can send the locator plugin when project is complete for final HTML/CSS Coding. Needs to be coded as a responsive design on a flexible grid (i.e. will auto adjust screen for desktop/tablet/mobile devices)
Target Market(s)
Business/Student/General Public, Mobile Office Kiosk Rental Station (Technology-Printing-Scanning-Faxing, etc...)
Industry/Entity Type
It Professional
Coding
Coded - Design and coding required
Number of Pages Required
1 page
Look and feel
Each slider illustrates characteristics of the customer's brand and the style your logo design should communicate.

```html
<!DOCTYPE html>
<html lang="en">
<head>
<meta charset="utf-8">
<title>TRAVo Kiosk</title>
<link href="https://fonts.googleapis.com/css2?family=Lato:wght@400;700;900&family=Montserrat:wght@400;700&display=swap" rel="stylesheet">
<style>
:root{
  --brand:#0a8ccf;
  --brand-dark:#2a7fb3;
  --red:#d9261c;
  --ink:#1b1b1b;
  --body:#555;
  --muted:#777;
  --panel:#f1f1f1;
  --navy:#1f3d6b;
  --footer:#2d2d2d;
}
*{box-sizing:border-box;margin:0;padding:0}
html,body{width:1200px;height:2209px;overflow:hidden}
body{position:relative;font-family:'Lato',sans-serif;color:var(--ink);background:#fff}
.abs{position:absolute}

.top-rule{left:0;top:0;width:1200px;height:3px;background:var(--brand)}
.site-header{left:0;top:3px;width:1200px;height:131px;background:#fff}
.brand{left:112px;top:40px;display:flex;align-items:center;gap:12px;font-size:34px;font-weight:700;color:var(--brand)}
.brand-mark{width:26px;height:26px;background:var(--brand);border-radius:50%}
.contact-line{right:110px;top:32px;display:flex;gap:14px;font-size:17px;color:#222;align-items:center}
.contact-line span{display:flex;align-items:center;gap:8px}
.main-nav{right:90px;top:74px;display:flex;gap:0;font-size:18px}
.main-nav a{display:block;padding:6px 20px;margin-left:22px;color:#222;text-decoration:none;letter-spacing:.3px}
.main-nav a.active{background:var(--brand);color:#fff;font-weight:700}

.hero{left:0;top:134px;width:1200px;height:490px;background:linear-gradient(90deg,#f4f5f6 0%,#e6e9ec 45%,#c9cfd4 70%,#b9aaa0 100%)}
.hero-title{left:110px;top:248px;font-size:35px;font-weight:700;line-height:38px;color:#111}
.hero-title em{font-style:normal;color:var(--brand)}
.hero-text{left:110px;top:336px;width:410px;font-size:15px;line-height:23px;color:#222}
.btn{display:inline-block;color:#fff;font-size:19px;text-align:center;line-height:37px;border-radius:2px}
.btn-red{left:110px;top:427px;width:118px;height:37px;background:var(--red)}
.dots{left:110px;top:492px;display:flex;gap:5px}
.dots i{width:8px;height:8px;border-radius:50%;background:#888}
.dots i.on{background:var(--brand)}

.service-panel{left:107px;top:601px;width:983px;height:300px;background:#fff}
.service{width:234px;top:618px}
.service .thumb{width:234px;height:146px}
.service h3{margin:20px 0 0 3px;font-size:23px;font-weight:400;color:#111}
.service p{margin:8px 0 0 3px;font-size:14.5px;line-height:21px;color:var(--body)}
.service .more{display:block;margin:12px 0 0 3px;font-size:14px;font-weight:900;letter-spacing:1.5px;color:var(--navy)}

.office{left:0;top:936px;width:1200px;height:298px;background:var(--panel)}
.section-title{font-size:35px;font-weight:400;color:#111}
.section-title em{font-style:normal;color:var(--brand)}
.office-title{left:110px;top:962px}
.office-text{left:110px;top:1018px;width:545px;font-size:14px;line-height:22px;color:var(--muted)}
.btn-blue{left:110px;top:1153px;width:118px;height:37px;background:var(--brand-dark)}
.office-img{left:698px;top:979px;width:392px;height:217px}

.clients-title{left:0;top:1273px;width:1200px;text-align:center}
.clients-sub{left:200px;top:1328px;width:800px;text-align:center;font-size:15px;line-height:23px;color:var(--muted)}
.clients-rule{left:522px;top:1385px;width:156px;height:3px;background:var(--brand)}
.avatar{width:128px;height:128px;border-radius:50%;border:4px solid #fff;box-shadow:0 0 0 1px #ccc;background:linear-gradient(#8a8f95,#3b3f45)}
.quote{width:305px;height:111px;background:#fff;border:1px solid #ddd;box-shadow:0 3px 0 -1px #e6e6e6;padding:14px 20px}
.quote:before{content:"";position:absolute;left:-9px;top:22px;width:16px;height:16px;background:#fff;border-left:1px solid #ddd;border-bottom:1px solid #ddd;transform:rotate(45deg)}
.quote p{font-size:12px;line-height:16px;color:var(--muted)}
.quote b{display:block;margin-top:4px;font-size:14px;color:var(--brand-dark)}

.map{left:0;top:1606px;width:1200px;height:347px;background:linear-gradient(135deg,#eee8d8,#e3e6cf 50%,#cfe0e8)}

.newsletter{left:0;top:1953px;width:1200px;height:206px;background:var(--brand)}
.news-title{left:0;top:1991px;width:1200px;text-align:center;font-family:'Montserrat',sans-serif;font-size:32px;color:#fff}
.news-title b{font-weight:700}
.news-sub{left:0;top:2038px;width:1200px;text-align:center;font-size:15px;color:#fff}
.news-input{left:383px;top:2078px;width:330px;height:44px;background:#fff;font-size:14px;color:#999;padding:13px 12px}
.news-btn{left:713px;top:2078px;width:101px;height:44px;background:var(--red);color:#fff;font-size:17px;font-weight:700;text-align:center;line-height:44px}

.site-footer{left:0;top:2159px;width:1200px;height:50px;background:var(--footer);color:#fff;font-size:13px;text-align:center;line-height:50px}
</style>
</head>
<body>
<div class="abs top-rule"></div>
<header class="abs site-header"></header>
<div class="abs brand"><span class="brand-mark"></span>TRAVo</div>
<div class="abs contact-line">
  <span><svg width="16" height="12" viewBox="0 0 16 12"><rect x="0.5" y="0.5" width="15" height="11" fill="#444"/><path d="M1 1l7 6 7-6" stroke="#fff" fill="none"/></svg>hello@travokiosk.net</span>
  <span><svg width="17" height="17" viewBox="0 0 24 24"><path fill="#444" d="M6.6 10.8a15 15 0 006.6 6.6l2.2-2.2c.3-.3.7-.4 1-.2 1.1.4 2.3.6 3.6.6.6 0 1 .4 1 1V20c0 .6-.4 1-1 1A17 17 0 013 4c0-.6.4-1 1-1h3.5c.6 0 1 .4 1 1 0 1.3.2 2.5.6 3.6.1.3 0 .7-.2 1z"/></svg>555-014-2090</span>
</div>
<nav class="abs main-nav">
  <a class="active">HOME</a><a>ABOUT US</a><a>SERVICES</a><a>PRODUCT</a><a>CONTACT US</a>
</nav>

<section class="abs hero" role="img" aria-label="Photo of a smiling couple using a self-service kiosk touchscreen in an airport"></section>
<h1 class="abs hero-title">Welcome To <em>TRAVo Kiosk</em><br>Technology</h1>
<p class="abs hero-text">Lorem Ipsum is simply dummy text of the printing and typeset-ting industry. Lorem Ipsum has been the industry's standard dummy text ever since the 1500s,</p>
<a class="abs btn btn-red">Read More</a>
<div class="abs dots"><i></i><i></i><i></i><i class="on"></i><i></i></div>

<div class="abs service-panel"></div>
<article class="abs service" style="left:118px">
  <div class="thumb" role="img" aria-label="Photo of a blue kiosk in a terminal hall" style="background:linear-gradient(135deg,#2f5fb0,#9c8a60)"></div>
  <h3>kiosk technology</h3>
  <p>Lorem ipsum dolor sit amet, con-sectetuer adipiscing elit,</p>
  <a class="more">READ MORE &raquo;</a>
</article>
<article class="abs service" style="left:361px">
  <div class="thumb" role="img" aria-label="Photo of a hand signing a printed document" style="background:linear-gradient(135deg,#d8dde2,#9aa4ae)"></div>
  <h3>Document Printing</h3>
  <p>Lorem ipsum dolor sit amet, con-sectetuer adipiscing elit,</p>
  <a class="more">READ MORE &raquo;</a>
</article>
<article class="abs service" style="left:604px">
  <div class="thumb" role="img" aria-label="Photo of hands placing paper on a scanner" style="background:linear-gradient(135deg,#c8ccd0,#4a5560)"></div>
  <h3>Paper Scaning</h3>
  <p>Lorem ipsum dolor sit amet, con-sectetuer adipiscing elit,</p>
  <a class="more">READ MORE &raquo;</a>
</article>
<article class="abs service" style="left:847px">
  <div class="thumb" role="img" aria-label="Photo of a fax machine on an office desk" style="background:linear-gradient(135deg,#eceae6,#b8b4ac)"></div>
  <h3>Document Faxing</h3>
  <p>Lorem ipsum dolor sit amet, con-sectetuer adipiscing elit,</p>
  <a class="more">READ MORE &raquo;</a>
</article>

<section class="abs office"></section>
<h2 class="abs section-title office-title">Welcome to <em>Mobile Office.</em></h2>
<p class="abs office-text">Where you need it. When you need it. TRAVo kiosks provide easy access for you to run your mobile office. Whether you nees to access the internet to research information, access email, download document or pay bills, were here to help , TRAVo kiosks also pro-vide you with the ability to print, scan, copy and fax document you need quickly, All at the touch of a button.</p>
<a class="abs btn btn-blue">Read More</a>
<div class="abs office-img" role="img" aria-label="Photo of a yellow self-service kiosk in an airport concourse" style="background:linear-gradient(135deg,#6b5a40,#e0a020 55%,#d9d4c8)"></div>

<h2 class="abs section-title clients-title">We Make Our <em>Client Happy</em></h2>
<p class="abs clients-sub">Northfield Textiles produces a wide variety of fabrics, many custom engineered, from polyester, cotton and blended yarns for a diverse customer base including:</p>
<div class="abs clients-rule"></div>

<div class="abs avatar" style="left:110px;top:1428px" role="img" aria-label="Portrait photo of a client"></div>
<div class="abs quote" style="left:272px;top:1431px">
  <p>Lorem ipsum dolor sit amet, consectetur adipis-celit. In elit enim, lobortis eu dignissim id, di rutrum nunc. Fusce eget magna eget urna aliquet vitae et lorem.</p>
  <b>Daniel Morrow</b>
</div>
<div class="abs avatar" style="left:624px;top:1428px" role="img" aria-label="Portrait photo of a client"></div>
<div class="abs quote" style="left:785px;top:1431px">
  <p>Lorem ipsum dolor sit amet, consectetur adipice lit. In elit enim, lobortis eu dignissim id, discomd rutrum nunc. Fusce eget magna eget urnaen aliquet vitae et lorem.</p>
  <b>Daniel Morrow</b>
</div>

<section class="abs map" role="img" aria-label="Store locator map of the south-eastern United States with search and filter controls"></section>

<section class="abs newsletter"></section>
<h2 class="abs news-title"><b>JOIN</b> OUR NEWSLETTER</h2>
<p class="abs news-sub">Lorem ipsum dolor sit amet, consectetuer there are adipiscing elit,</p>
<div class="abs news-input">Enter Your Email Address</div>
<div class="abs news-btn">Subscribe</div>

<footer class="abs site-footer">Copy Right 2015 TRAVo. All Right Reserve</footer>
</body>
</html>
```